Nobre Lente Lusitana - business card

Create a business card for my eyewear (glasses) store. The concept is based in handcrafted glasses (as well as common frames and 3d printed), clean, and elegant. The business card could be black (white letters and symbols) or white (black letters and symbols) but we are open to new suggestions. It must be sober and elegant.
The name Nobre Lente Lusitana means Royal/Real Portuguese Optical Store.
Our concept should be inspired by the pictures attatched bellow.
I would like it to be classic and elegant as business cards for bankers.
Our first selected logo is also available in attachment files.

Target Market(s)

For business meetings with investors, supliers and fairs

Industry/Entity Type

Eyewear

Contact Information for Business Card

Some random business cards in attachment that we like. Don't be closed to it, we like freedom of think.

Font styles to use
Serif
Sans Serif

Colors
404040
e9e9e9
fbfbfb
000000
85abd3
0255a3
f7fbfd
959595

Requirements
Must have
• Must be elegant, simple.
• Must present our brand new logo (slight variations are welcome, the logo is not closed yet). See our temporary logo in attachment.
• Black (or dark grey), white (or light grey) and a third slight color.
• This third slight color could be dark blue or grayish blue.
• Info:
• Fernando Amaral (name)
• famaral@nobrelentelusitana.example
• +351 936204518
• www.nobrelentelusitana.example
Nice to have
• Black and white or with serious colors such as dark blue or greyish blue.
• Could also have water mark with our logo (big size) in the background (inspired in KVN bank credit card design)
Should not have
• Hysteric colora or shapes

```html
<!DOCTYPE html>
<html lang="pt">
<head>
<meta charset="utf-8">
<title>Nobre Lente Lusitana – Cartão de visita</title>
<link rel="stylesheet" href="https://fonts.googleapis.com/css2?family=Fira+Sans+Condensed:wght@400;700&family=Bitter:wght@400&display=swap">
<style>
  :root {
    --backdrop: #e9e9e9;
    --card: #2b2b2b;
    --card-edge: #404040;
    --ink: #fbfbfb;
    --ink-soft: #e9e9e9;
    --accent: #85abd3;
  }
  * { margin: 0; padding: 0; box-sizing: border-box; }
  html, body { width: 1200px; height: 900px; overflow: hidden; }
  body {
    background: var(--backdrop);
    display: flex;
    flex-direction: column;
    align-items: center;
    justify-content: center;
    gap: 60px;
  }
  .card {
    width: 580px;
    height: 350px;
    background: var(--card);
    border: 1px solid var(--card-edge);
    border-radius: 4px;
    position: relative;
    color: var(--ink);
    box-shadow: 0 10px 30px rgba(0,0,0,0.18);
    overflow: hidden;
  }
  .card__band {
    position: absolute;
    left: 0; right: 0; bottom: 0;
    height: 4px;
    background: var(--accent);
  }
  .wordmark {
    font-family: "Fira Sans Condensed", sans-serif;
    font-weight: 400;
    text-transform: uppercase;
    color: var(--ink);
    display: flex;
    align-items: center;
    gap: 12px;
    letter-spacing: 0.12em;
    white-space: nowrap;
  }
  .wordmark__dot {
    width: 14px; height: 14px;
    border: 2px solid var(--accent);
    border-radius: 50%;
    flex: none;
  }
  .card--front { display: flex; align-items: center; justify-content: center; }
  .card--front .wordmark { font-size: 30px; }
  .card--back .wordmark {
    position: absolute;
    left: 34px;
    bottom: 44px;
    font-size: 17px;
  }
  .contact {
    position: absolute;
    left: 290px;
    top: 110px;
  }
  .contact__name {
    font-family: "Fira Sans Condensed", sans-serif;
    font-weight: 700;
    font-size: 24px;
    letter-spacing: 0.03em;
    text-transform: uppercase;
    white-space: nowrap;
  }
  .contact__rule {
    width: 36px;
    height: 2px;
    background: var(--accent);
    margin: 10px 0 12px;
  }
  .contact__line {
    font-family: "Bitter", serif;
    font-size: 13px;
    line-height: 1.5;
    color: var(--ink-soft);
    white-space: nowrap;
  }
</style>
</head>
<body>
  <section class="card card--front" aria-label="Frente do cartão">
    <div class="wordmark"><span class="wordmark__dot"></span>Nobre Lente Lusitana</div>
    <div class="card__band"></div>
  </section>

  <section class="card card--back" aria-label="Verso do cartão">
    <div class="wordmark"><span class="wordmark__dot"></span>Nobre Lente Lusitana</div>
    <div class="contact">
      <p class="contact__name">Fernando Amaral</p>
      <div class="contact__rule"></div>
      <p class="contact__line">+351 936 204 518</p>
      <p class="contact__line">famaral@nobrelentelusitana.example</p>
      <p class="contact__line">www.nobrelentelusitana.example</p>
    </div>
    <div class="card__band"></div>
  </section>
</body>
</html>
```